New menu design for small coffee shop

I need to design a new menu for a small cafe called The Kettle Wren. I've attached pictures of the old menu to give an idea, I really want a completely new look though. You'll notice that the food, coffee and drinks are currently on separate menus, I want all of this to be on one menu. We want to add images of the food before we print the menu, so ideally you will leave spaces for images of the food.
I'm open to suggestions on paper size and how its folded etc.
I've also attached a word file which has changes for the new menu; some are pricing updates, some are completely different.
Our facepage page is https://www.facepage.example/thekettlewren/ might give you an idea of what we're about.
Any other questions let me know.
Cafe

```html
<!DOCTYPE html>
<html lang="en">
<head>
<meta charset="utf-8">
<title>The Kettle Wren – Summer Menu</title>
<link rel="stylesheet" href="https://fonts.googleapis.com/css2?family=Architects+Daughter&family=Kaushan+Script&family=Mulish:wght@400;700&family=Questrial&display=swap">
<style>
  :root{
    --backdrop:#d4d4d4;
    --paper:#ffffff;
    --ink:#2b2b2b;
    --ink-soft:#4a4a4a;
    --mark:#eeeeee;
    --brick:#a8674a;
    --brick-light:#e4c1a8;
    --food-warm:#d9a77a;
    --food-cool:#c9d3c2;
    --cafe-shade:#3c3a36;
    --cafe-grass:#6f9a48;
    --dessert:#e2a6b4;
  }
  *{box-sizing:border-box;margin:0;padding:0}
  html,body{width:1200px;height:1000px;overflow:hidden}
  body{background:var(--backdrop);font-family:"Questrial",sans-serif;color:var(--ink);position:relative}
  .sheet{position:absolute;left:40px;width:1120px;height:470px;background:var(--paper);overflow:hidden;box-shadow:0 2px 6px rgba(0,0,0,.18)}
  .sheet--drinks{top:16px}
  .sheet--food{top:514px}
  .seal{position:absolute;border:10px solid var(--mark);border-radius:50%;pointer-events:none}
  .col{position:absolute;top:18px;font-size:10.5px;line-height:11.6px}
  .section-title{font-family:"Architects Daughter",cursive;font-size:15px;letter-spacing:.5px;text-transform:uppercase;margin-bottom:4px;line-height:18px}
  .section-title small{font-family:"Questrial",sans-serif;font-size:9.5px;text-transform:none;letter-spacing:0}
  .group{font-family:"Mulish",sans-serif;font-weight:700;margin-top:7px}
  .group .price{font-family:"Questrial",sans-serif;font-weight:400}
  .row{display:flex}
  .row .name{flex:1}
  .row .price{width:44px;text-align:right}
  .head-sizes{display:flex;justify-content:flex-end;font-size:10px}
  .head-sizes span{width:44px;text-align:right}

  .col--hot{left:22px;width:260px}
  .col--cold{left:300px;width:230px}

  .cover{position:absolute;left:760px;top:14px;width:340px;text-align:center}
  .cover__sign{height:150px;background:linear-gradient(135deg,var(--brick-light),var(--brick) 55%,#7d4a35);display:flex;align-items:center;justify-content:center;gap:8px;color:#fff;font-family:"Mulish",sans-serif;font-weight:700;font-size:17px;letter-spacing:2px;text-transform:uppercase}
  .cover__sign .dot{width:14px;height:14px;border-radius:50%;background:#fff}
  .cover__title{font-family:"Kaushan Script",cursive;font-size:34px;margin-top:12px;line-height:40px}
  .cover__rule{display:block;margin:0 auto 12px}
  .cover__hours{font-size:15px;line-height:18px;margin-bottom:10px}
  .cover__info{font-size:11px;line-height:14px;color:var(--ink-soft)}
  .cover__photo{width:200px;height:115px;margin:20px 0 0 20px;background:linear-gradient(180deg,#b8c6cf 0%,#d8d4cc 40%,var(--cafe-shade) 70%,var(--cafe-grass) 100%)}

  .col--breakfast{left:24px;width:320px}
  .col--lunch{left:372px;width:330px}
  .col--salads{left:730px;width:360px}
  .item{margin-bottom:8px;overflow:hidden}
  .item__name{font-family:"Mulish",sans-serif;font-weight:700}
  .item__price{text-align:right}
  .food-shot{float:right;width:96px;height:62px;border-radius:6px;margin:2px 0 4px 8px}
  .food-shot--warm{background:linear-gradient(135deg,#f2e6d6,var(--food-warm))}
  .food-shot--cool{background:linear-gradient(135deg,#eef1ea,var(--food-cool))}
  .desserts{height:220px;margin-top:6px;border-radius:8px;background:linear-gradient(135deg,#f3dfc4,var(--dessert) 55%,#a97a5a)}
</style>
</head>
<body>

<section class="sheet sheet--drinks">
  <div class="seal" style="left:80px;top:40px;width:400px;height:400px"></div>

  <div class="col col--hot">
    <div class="row"><h2 class="section-title name">Hot Beverages</h2></div>
    <div class="head-sizes"><span>Small</span><span>Large</span></div>
    <div class="row"><span class="name">Cappuccino</span><span class="price">$3.5</span><span class="price">$4.5</span></div>
    <div class="row"><span class="name">Cafe Latte</span><span class="price">$3.5</span><span class="price">$4.5</span></div>
    <div class="row"><span class="name">Chai Latte</span><span class="price">$3.8</span><span class="price">$4.8</span></div>
    <div class="row"><span class="name">Flat White</span><span class="price">$3.5</span><span class="price">$4.5</span></div>
    <div class="row"><span class="name">Mocha</span><span class="price">$3.8</span><span class="price">$4.8</span></div>
    <div class="row"><span class="name">White Mocha</span><span class="price">$3.8</span><span class="price">$4.8</span></div>
    <div class="row"><span class="name">Hot Chocolate</span><span class="price">$3.8</span><span class="price">$4.8</span></div>
    <div class="row"><span class="name">Extreme Hot Chocolate</span><span class="price">$4.8</span><span class="price">$5.8</span></div>
    <div class="row"><span class="name">White Hot Chocolate</span><span class="price">$3.8</span><span class="price">$4.8</span></div>
    <div class="row"><span class="name">Long Black</span><span class="price">$3.5</span><span class="price">$4.5</span></div>
    <div class="row"><span class="name">Cafe Le Cream</span><span class="price">$3.5</span><span class="price">$4.5</span></div>
    <div class="row"><span class="name">Espresso 30ml</span><span class="price">$4.0</span><span class="price">$3.5</span></div>
    <div class="row"><span class="name">Double Espresso</span><span class="price">$3.5</span><span class="price"></span></div>
    <div class="row"><span class="name">Piccolo</span><span class="price">$3.5</span><span class="price"></span></div>
    <div class="row"><span class="name">Macchiato - Short</span><span class="price">$4.5</span><span class="price"></span></div>
    <div class="row"><span class="name">Macchiato - Long</span><span class="price"></span><span class="price">$5.5</span></div>
    <div class="row"><span class="name">Iced Latte</span><span class="price"></span><span class="price"></span></div>

    <div class="group">Extras</div>
    <div class="row"><span class="name">Extra Shot</span><span class="price"></span><span class="price">$0.5</span></div>
    <div class="row"><span class="name">Coffee Syrups</span><span class="price"></span><span class="price">$0.5</span></div>
    <div class="row"><span class="name">Hazelnut, Caramel, Vanilla</span><span class="price">$4.0</span><span class="price"></span></div>

    <div class="row group"><span class="name">Leafline Tea</span><span class="price">$4.0</span><span class="price"></span></div>
    <div class="row"><span class="name">English Breakfast</span></div>
    <div class="row"><span class="name">Earl Grey</span></div>

    <div class="row group"><span class="name">Leafline Herbal Tea</span><span class="price">$4.0</span><span class="price"></span></div>
    <div class="row"><span class="name">Lemon &amp; Ginger</span></div>
    <div class="row"><span class="name">Green Tea</span></div>
    <div class="row"><span class="name">Oolong</span></div>

    <div class="row group"><span class="name">Iced Tea</span><span class="price">$4.5</span><span class="price"></span></div>
    <div class="row"><span class="name">Fruitalicious</span></div>
    <div class="row"><span class="name">Lemongrass &amp; Ginger</span></div>
  </div>

  <div class="col col--cold">
    <div class="row group" style="margin-top:0"><span class="name">Milkshakes</span><span class="price">$5.0</span></div>
    <div class="row"><span class="name">Chocolate, Vanilla, Caramel, Strawberry</span></div>

    <div class="row group"><span class="name">Extreme Milkshakes</span><span class="price">$10.0</span></div>
    <div>Chocolate Infusion</div>
    <div>Extreme Caramel</div>
    <div>Vanilla &amp; White Chocolate Mayhem</div>
    <div>Strawberry Fields</div>
    <div>Bananarama</div>
    <div>Mocha Smash</div>
    <div>Brownie Bonanza</div>

    <div class="row group"><span class="name">Frappes</span><span class="price">$6.0</span></div>
    <div>Mango</div>
    <div>Pineapple &amp; Mango</div>
    <div>Pineapple, Mint &amp; Apple</div>
    <div>Chocolate</div>
    <div>Coffee</div>

    <div class="row group"><span class="name">Iced Drinks</span><span class="price">$6.5</span></div>
    <div>Iced Chocolate</div>
    <div>Iced Coffee</div>

    <div class="row group"><span class="name">Smoothies</span><span class="price">$6.5</span></div>
    <div>Mango</div>
    <div>Banana</div>

    <div class="row group"><span class="name">Fresh Fruit Juice</span><span class="price">$5.0</span></div>
    <div>Seasonal Fruit</div>

    <div class="group">Soft Drinks</div>
    <div class="row"><span class="name">375 ml can</span><span class="price">$3.5</span></div>
    <div class="row"><span class="name">Burnett drinks</span><span class="price">$4.5</span></div>

    <div class="row group"><span class="name">Bottled Water</span><span class="price">$2.5</span></div>

    <div class="group">Juice</div>
    <div class="row"><span class="name">Orange Juice 500 ml</span><span class="price">$4.5</span></div>
    <div class="row"><span class="name">Orange Juice 250 ml</span><span class="price">$3.0</span></div>
    <div class="row"><span class="name">Apple &amp; Black Current 250 ml</span><span class="price">$3.0</span></div>
  </div>

  <div class="cover">
    <div class="cover__sign" role="img" aria-label="Cafe name sign on a brick wall"><span class="dot"></span>The Kettle Wren</div>
    <h1 class="cover__title">Summer Menu</h1>
    <svg class="cover__rule" width="190" height="8" viewBox="0 0 190 8" aria-hidden="true"><path d="M2 6 Q95 0 188 3" stroke="#555" stroke-width="3" fill="none" stroke-linecap="round"/></svg>
    <p class="cover__hours">Open 7 Days<br>7am - 2pm</p>
    <p class="cover__info">Check us out on facepage<br>www.facepage.example/thekettlewren<br>Call us on (07) 5550 1742 for<br>party bookings or<br>catering for you special event</p>
    <div class="cover__photo" role="img" aria-label="Photo of the cafe shopfront with outdoor seating"></div>
  </div>
</section>

<section class="sheet sheet--food">
  <div class="seal" style="left:120px;top:30px;width:420px;height:420px"></div>

  <div class="col col--breakfast">
    <h2 class="section-title">All Day Breakfast Menu</h2>
    <div class="item">
      <div class="food-shot food-shot--warm" role="img" aria-label="Photo of the big breakfast plate"></div>
      <div class="item__name">Wren Breakfast</div>
      <div>grilled smokey bacon, eggs, thick pork sausage, grilled mushroom topped with a lightly spiced tomato chutney, grilled tomato, lamb cutlet and hash brown with Turkish bread</div>
      <div class="item__price">$21.0</div>
    </div>
    <div class="item"><div class="row"><span class="name item__name">Eggs on Turkish toast</span><span class="price">$8.0</span></div></div>
    <div class="item"><div class="row"><span class="name item__name">Bacon and eggs on Turkish toast with grilled tomato</span><span class="price">$15.0</span></div></div>
    <div class="item">
      <div class="food-shot food-shot--cool" role="img" aria-label="Photo of eggs benedict"></div>
      <div class="item__name">Eggs Benedict</div>
      <div>poached eggs with bacon, ham or smoked salmon and wilted baby spinach and finished with Hollandaise Sauce</div>
      <div class="item__price">$18.0</div>
    </div>
    <div class="item">
      <div class="item__name">Veggie Brekki</div>
      <div class="row"><span class="name">our own special smashed avocado on grilled Portobello mushroom, with poached eggs, Danish feta and baby spinach</span><span class="price">$16.0</span></div>
    </div>
    <div class="item">
      <div class="item__name">High Protein Overnight Oats</div>
      <div class="row"><span class="name">our own protein enriched Greek yoghurt, oats and honey, topped with sliced banana</span><span class="price">$15.0</span></div>
    </div>
    <div class="item">
      <div class="item__name">Omelette of the Day</div>
      <div class="row"><span class="name">served with toasted Turkish bread and grilled tomato</span><span class="price">$18.0</span></div>
    </div>
  </div>

  <div class="col col--lunch">
    <div class="item">
      <div class="item__name">Waffles</div>
      <div>freshly toasted waffles, maple syrup, strawberries and banana with ice cream or cream</div>
      <div class="item__price">$15.0</div>
    </div>
    <div class="item"><div class="row"><span class="name item__name">Fruit Toast</span><span class="price">$6.0</span></div></div>
    <div class="item"><div class="row"><span class="name item__name">Multigrain or White Toast with butter</span><span class="price">$4.0</span></div></div>
    <h2 class="section-title">Lunch Menu <small>(from 11:30)</small></h2>
    <div class="item">
      <div class="item__name">BLT</div>
      <div class="row"><span class="name">roast garlic aioli, tomato chutney, smoked bacon, mixed lettuce and tomato on toasted Turkish bread with fries</span><span class="price">$12.0</span></div>
    </div>
    <div class="item">
      <div class="item__name">Chicken Caesar Burger or Wrap</div>
      <div>marinated chicken, smoked bacon, Parmesan cheese, and cos lettuce in a toasted Turkish bread or wrap, with fries</div>
      <div class="item__price">$15.0</div>
    </div>
    <div class="item">
      <div class="food-shot food-shot--warm" role="img" aria-label="Photo of the beef burger with fries"></div>
      <div class="item__name">Wren Beef Burger</div>
      <div class="row"><span class="name">juicy beef patty, smoked bacon, mixed lettuce, tomato, beetroot, caramelised onion with relish and aioli, on grilled Turkish bread with fries</span><span class="price">$17.0</span></div>
    </div>
    <div class="item">
      <div class="item__name">Caesar Salad</div>
      <div class="row"><span class="name">crispy cos lettuce, smokey bacon, Parmesan cheese, herbed croutons all tossed together with Caesar dressing and finished with a poached egg</span><span class="price">$14.0</span></div>
    </div>
    <div class="item"><div class="row"><span class="name item__name">Add chicken, salmon or avocado</span><span class="price">$3.0</span></div></div>
  </div>

  <div class="col col--salads">
    <div class="item">
      <div class="item__name">Thai Beef Salad</div>
      <div>marinated slices of tender eye fillet steak, mixed lettuce, julianne vegetables, fresh coriander and mint with our special Thai dressing</div>
      <div class="item__price">$17.0</div>
    </div>
    <div class="item">
      <div class="food-shot food-shot--cool" role="img" aria-label="Photo of the quinoa salad"></div>
      <div class="item__name">Quinoa Salad</div>
      <div class="row"><span class="name">roast root vegetables with pomegranate, walnuts, baby spinach and balsamic dressing</span><span class="price">$15.0</span></div>
    </div>
    <div class="item">
      <div class="item__name">Chips</div>
      <div class="row"><span class="name" style="padding-left:22px">Small</span><span class="price">$4.0</span></div>
      <div class="row"><span class="name" style="padding-left:22px">Large</span><span class="price">$7.0</span></div>
    </div>
    <h2 class="section-title" style="margin-bottom:0">Cakes/Desserts</h2>
    <div style="font-size:9.5px">(check the blackboard)</div>
    <div class="desserts" role="img" aria-label="Photo collage of cakes, muffins, waffles, shakes and coffee"></div>
  </div>
</section>

</body>
</html>
```